Traffic product supplier - Temporary Raised Pavement Markers

We need a flyer design that will grab the customer's eye to the product (TRPMs) and entice curiosity to the business. Showing 1 product but promoting other products. The following information should be included:
- Logo (attached)
- Sale Product image (Temporary Road Pavement Marker AKA Press and Holds)
- Product wording (attached word document)

Happy for you to add/amend wording for grammatical purpose and other images that show it is a sale flyer.

Background on KLV - We are a thermoplastic manufacturer for road markings and traffic product supplier. KLV specializes in producing high quality hotmelt thermoplastic that meet Australian Standard AS4049.2. We are able to produce other specifications as required by the customer.

Would like the colour scheme to be similar to the logo.

If you need more information let me know.

Target Market(s)

Asphalt industry / road builders

Font styles to use
Serif
Sans Serif

Requirements
Must have
• - Kelvoro Lane Ventures (My company name)
- Contact details:
- 02 8417 2530
- marcus.t@klvsupplyco.com.au
- info@klvsupplyco.com.au
-www.klvmtq.com

- Attached images.
-Title (Temporary Road Pavement Markers)

```html
<!DOCTYPE html>
<html lang="en">
<head>
<meta charset="utf-8">
<title>Temporary Raised Pavement Markers – KLV</title>
<link rel="stylesheet" href="https://fonts.googleapis.com/css2?family=Oswald:wght@500;600&family=Cabin:ital,wght@0,400;0,500;1,700&display=swap">
<style>
:root{
  --brand-blue:#1a4fa8;
  --deep-blue:#0f3d8f;
  --badge-red:#c4202f;
  --text-grey:#3a3d42;
  --band-grey:#b4b7bb;
  --page:#ffffff;
  --backdrop:#e9eaec;
}
*{margin:0;padding:0;box-sizing:border-box}
html,body{width:1200px;height:872px;overflow:hidden;background:var(--backdrop)}
.flyer{position:absolute;left:302px;top:15px;width:596px;height:842px;background:var(--page);overflow:hidden;font-family:"Cabin",sans-serif}
.flyer-art{position:absolute;left:0;top:0;width:596px;height:842px}
.title{position:absolute;left:38px;top:28px;white-space:nowrap;font-family:"Oswald",sans-serif;font-weight:600;font-size:36px;color:var(--deep-blue);letter-spacing:.2px}
.brand{position:absolute;left:40px;top:318px;display:flex;align-items:center;gap:8px}
.brand-square{width:22px;height:22px;background:var(--brand-blue)}
.brand-name{font-family:"Oswald",sans-serif;font-weight:600;font-size:46px;color:var(--brand-blue);line-height:1}
.tagline{position:absolute;left:22px;top:389px;font-size:7px;font-style:italic;font-weight:700;color:var(--deep-blue)}
.intro{position:absolute;left:20px;top:418px;width:362px;font-size:11.4px;line-height:14.5px;color:var(--brand-blue)}
.thumbs{position:absolute;left:30px;top:507px;display:flex;gap:14px}
.thumb{width:104px;height:76px;border-radius:3px}
.thumb-yellow{background:linear-gradient(160deg,#e2b21c,#b98e12 70%,#d9d9d9)}
.thumb-red{background:linear-gradient(170deg,#c9283a 0 14%,#eef0f2 15%,#c9cdd1)}
.thumb-white{background:linear-gradient(170deg,#9aa4b2 0 14%,#f1f2f4 15%,#c6c9cd)}
.price-badge{position:absolute;left:402px;top:417px;width:170px;height:170px}
.price-text{position:absolute;left:402px;top:464px;width:170px;text-align:center;font-family:"Oswald",sans-serif;font-weight:500;font-size:26px;line-height:39px;color:#fff}
.details{position:absolute;left:20px;top:604px;width:460px;font-size:11px;line-height:14.5px;color:var(--text-grey)}
.features{position:absolute;left:20px;top:670px;list-style:none;font-size:11.5px;color:var(--text-grey)}
.features li{display:flex;align-items:center;gap:10px;height:20px}
.features svg{width:12px;height:12px}
.divider{position:absolute;left:20px;top:763px;width:448px;border-top:2px dashed var(--brand-blue)}
.contacts{position:absolute;left:22px;top:779px;list-style:none;font-size:13px;color:var(--text-grey)}
.contacts li{display:flex;align-items:center;gap:6px;height:19px}
.contacts svg{width:12px;height:12px}
.phone{position:absolute;left:270px;top:784px;display:flex;align-items:center;gap:10px;font-family:"Oswald",sans-serif;font-weight:500;font-size:28px;color:var(--brand-blue);line-height:1}
.phone svg{width:28px;height:30px}
.phone-note{position:absolute;left:268px;top:820px;font-size:11px;font-style:italic;font-weight:700;color:var(--brand-blue)}
</style>
</head>
<body>
<div class="flyer">
  <svg class="flyer-art" viewBox="0 0 596 842">
    <defs>
      <linearGradient id="sceneTone" x1="0" y1="0" x2="0" y2="1">
        <stop offset="0" stop-color="#eef3f8"/>
        <stop offset=".14" stop-color="#c9d6e2"/>
        <stop offset=".19" stop-color="#b39a62"/>
        <stop offset=".3" stop-color="#7d6e4a"/>
        <stop offset=".4" stop-color="#3a3e44"/>
        <stop offset=".8" stop-color="#1e2229"/>
      </linearGradient>
    </defs>
    <rect role="img" aria-label="Country road photo with three temporary raised pavement markers in yellow, red and white" x="0" y="0" width="596" height="842" fill="url(#sceneTone)"/>
    <path fill="var(--brand-blue)" d="M180 258C370 262 520 400 596 575V640C500 420 360 290 180 275Z"/>
    <path fill="var(--band-grey)" d="M0 272C260 250 480 380 596 630V842H0Z"/>
    <path fill="#ffffff" d="M0 284C300 300 500 480 545 842H536C490 500 300 310 0 296Z"/>
    <path fill="#ffffff" d="M0 298C300 318 480 520 505 842H0Z"/>
  </svg>

  <h1 class="title">Temporary Raised Pavement Markers</h1>

  <div class="brand"><span class="brand-square"></span><span class="brand-name">KLV</span></div>
  <p class="tagline">"Keeping Every Lane Clearly Marked"</p>

  <p class="intro">Temporary road pavement markers, also known as press 'n' holds, are a great short-term solution to mark asphalt and pavements before permanent line marking takes place. They provide a way to delineate lanes and edges before the permanent longitudinal line marking process takes place.</p>

  <div class="thumbs">
    <div class="thumb thumb-yellow" role="img" aria-label="Yellow temporary pavement marker"></div>
    <div class="thumb thumb-red" role="img" aria-label="White marker with red reflective strip"></div>
    <div class="thumb thumb-white" role="img" aria-label="White marker with white reflective strip"></div>
  </div>

  <svg class="price-badge" viewBox="0 0 170 170" aria-hidden="true">
    <polygon fill="var(--badge-red)" points="85,0 96,14 110,4 116,20 133,15 133,32 150,33 144,49 160,56 148,68 162,79 148,88 160,101 144,106 150,122 133,123 133,140 116,136 110,152 96,142 85,156 74,142 60,152 54,136 37,140 37,123 20,122 26,106 10,101 22,88 8,79 22,68 10,56 26,49 20,33 37,32 37,15 54,20 60,4 74,14" transform="translate(0 7)"/>
  </svg>
  <div class="price-text">$0.40 EX GST<br>PER TRPM</div>

  <p class="details">TRPMs or press 'n' holds are available in yellow or white and come with a Class 1A reflective strip applied to tough high impact plastic. They are an economical solution for making newly laid roads safer. An easy to remove clear cover protects the reflective film during sealing and is easily ripped off afterwards.</p>

  <ul class="features">
    <li><svg viewBox="0 0 12 12"><circle cx="6" cy="6" r="6" fill="var(--brand-blue)"/><path d="M3.3 6.2 5.2 8 8.8 4.2" stroke="#fff" stroke-width="1.4" fill="none"/></svg>Dimensions: 100 mm long x 50 mm high x 25 mm wide</li>
    <li><svg viewBox="0 0 12 12"><circle cx="6" cy="6" r="6" fill="var(--brand-blue)"/><path d="M3.3 6.2 5.2 8 8.8 4.2" stroke="#fff" stroke-width="1.4" fill="none"/></svg>Double sided Class 1A Reflective</li>
    <li><svg viewBox="0 0 12 12"><circle cx="6" cy="6" r="6" fill="var(--brand-blue)"/><path d="M3.3 6.2 5.2 8 8.8 4.2" stroke="#fff" stroke-width="1.4" fill="none"/></svg>Clear cover for reflective protection</li>
    <li><svg viewBox="0 0 12 12"><circle cx="6" cy="6" r="6" fill="var(--brand-blue)"/><path d="M3.3 6.2 5.2 8 8.8 4.2" stroke="#fff" stroke-width="1.4" fill="none"/></svg>Available in all white, and red (reflective strip) and white, all yellow and all blue</li>
  </ul>

  <div class="divider"></div>

  <ul class="contacts">
    <li><svg viewBox="0 0 12 12"><circle cx="6" cy="6" r="6" fill="var(--brand-blue)"/><rect x="2.8" y="3.8" width="6.4" height="4.4" fill="none" stroke="#fff" stroke-width="1"/><path d="M2.8 3.8 6 6.4 9.2 3.8" stroke="#fff" fill="none" stroke-width="1"/></svg>info@klvsupplyco.com.au</li>
    <li><svg viewBox="0 0 12 12"><circle cx="6" cy="6" r="6" fill="var(--brand-blue)"/><rect x="2.8" y="3.8" width="6.4" height="4.4" fill="none" stroke="#fff" stroke-width="1"/><path d="M2.8 3.8 6 6.4 9.2 3.8" stroke="#fff" fill="none" stroke-width="1"/></svg>marcus.t@klvsupplyco.com.au</li>
    <li><svg viewBox="0 0 12 12"><circle cx="6" cy="6" r="6" fill="var(--brand-blue)"/><circle cx="6" cy="6" r="3.4" fill="none" stroke="#fff" stroke-width="1"/><path d="M2.6 6H9.4M6 2.6V9.4" stroke="#fff" stroke-width="1"/></svg>www.klvmtq.com</li>
  </ul>

  <div class="phone">
    <svg viewBox="0 0 28 30" aria-hidden="true"><rect x="9" y="1" width="14" height="27" rx="2.5" fill="var(--brand-blue)"/><rect x="11.5" y="4" width="9" height="17" fill="#fff"/><path d="M7 9C3 13 3 19 7 23" stroke="var(--brand-blue)" stroke-width="2.4" fill="none"/></svg>
    <span>02 8417 2530</span>
  </div>
  <p class="phone-note">for more information please contact us</p>
</div>
</body>
</html>
```